Brand New Church Business Card Design. Needs to appeal to high school students, professionals.

Business Card. Bold lines and colors. Simple font. This is a new church looking to attract new families who have moved to the area. Business professionals mostly. have a working logo. may need a little tweaking. Church is designed to do excellent ministries for students and children. Like business card design in box on mark vault homepage. Want a front and back side. Prefer colors to match the logo. But will lean on designers preferences and wisdom. DO NOT WANT A CROSS OR RELIGIOUS SYMBOL on the card.

Target Market(s)

Families, Professionals, Students

Industry/Entity Type

High School

Contact Information for Business Card

SaltRock ChurchSaltRock.atForrest Coulter904-515-8349Forrest@PineHollow.at

Font styles to use
Sans Serif

Colors
0255a3
ffffff

Requirements
Must have
• Bold colors. Very Masculine. Creative
Nice to have
• On printnook.markvault.com homepage in the business card design box. the card with the black, blue and gray looks really sharp. matches our logos.
Should not have
• no crosses or religious symbols.

```html
<!DOCTYPE html>
<html lang="en">
<head>
<meta charset="utf-8">
<title>PineHollow Church – Business Card</title>
<link href="https://fonts.googleapis.com/css2?family=Open+Sans:wght@400;600;800&display=swap" rel="stylesheet">
<style>
  :root {
    --brand-blue: #0255a3;
    --accent-blue: #2a86c9;
    --ink: #111111;
    --card-black: #0c0c0c;
    --paper: #ffffff;
    --backdrop: #e4e4e4;
    --text-grey: #333333;
    --ghost: #f3f4f6;
  }
  * { margin: 0; padding: 0; box-sizing: border-box; }
  html, body { width: 1200px; height: 852px; overflow: hidden; }
  body {
    background: var(--backdrop);
    font-family: "Open Sans", Arial, sans-serif;
    position: relative;
  }
  .card {
    position: absolute;
    width: 520px;
    height: 297px;
    border-radius: 16px;
    overflow: hidden;
    box-shadow: 0 4px 12px rgba(0,0,0,0.18);
  }
  .card-front {
    left: 50px; top: 278px;
    background: var(--card-black);
    display: flex; align-items: center; justify-content: center;
  }
  .card-back {
    left: 630px; top: 278px;
    background: var(--paper);
  }
  .brand {
    display: flex; align-items: center; gap: 14px;
  }
  .brand-dot {
    border-radius: 50%;
    background: var(--accent-blue);
    flex: none;
  }
  .brand-name {
    font-weight: 800;
    line-height: 1;
    letter-spacing: -0.5px;
  }
  .card-front .brand-dot { width: 96px; height: 96px; }
  .card-front .brand-name { color: var(--paper); font-size: 38px; }

  .back-brand { position: absolute; right: 36px; top: 34px; }
  .back-brand .brand-dot { width: 64px; height: 64px; background: var(--brand-blue); }
  .back-brand .brand-name { color: var(--ink); font-size: 26px; }

  .ghost-circle {
    position: absolute; left: 80px; top: 40px;
    width: 190px; height: 190px; border-radius: 50%;
    background: var(--ghost);
  }
  .wordmark {
    position: absolute; left: 34px; top: 104px;
    font-weight: 800; font-size: 22px; color: var(--ink);
    letter-spacing: -0.5px;
  }
  .person {
    position: absolute; left: 34px; top: 160px;
    font-size: 19px; font-weight: 600; color: var(--text-grey);
  }
  .person .first { color: var(--brand-blue); }
  .contacts {
    position: absolute; left: 34px; top: 194px;
    list-style: none;
    font-size: 13px; color: var(--text-grey);
  }
  .contacts li { display: flex; align-items: center; gap: 10px; height: 20px; }
  .contacts svg { width: 13px; height: 13px; fill: var(--brand-blue); flex: none; }
  .contacts .hl { color: var(--brand-blue); }
  .stripe { position: absolute; left: 0; bottom: 0; width: 520px; height: 297px; }
</style>
</head>
<body>
  <section class="card card-front" aria-label="Card front">
    <div class="brand">
      <span class="brand-dot"></span>
      <span class="brand-name">PineHollow Church</span>
    </div>
  </section>

  <section class="card card-back" aria-label="Card back">
    <div class="ghost-circle"></div>
    <div class="brand back-brand">
      <span class="brand-dot"></span>
      <span class="brand-name">PineHollow Church</span>
    </div>
    <p class="wordmark">PineHollow Church</p>
    <p class="person"><span class="first">Dwayne</span> Pellish</p>
    <ul class="contacts">
      <li><svg viewBox="0 0 16 16"><path d="M3 1h3l1 4-2 1c1 2 3 4 5 5l1-2 4 1v3c0 1-1 2-2 2C7 15 1 9 1 3c0-1 1-2 2-2z"/></svg>904-555-0172</li>
      <li><svg viewBox="0 0 16 16"><path d="M1 3h14v10H1z M1 3l7 6 7-6" stroke="#fff" stroke-width="1"/></svg>Dwayne@PineHollow.at</li>
      <li><svg viewBox="0 0 16 16"><circle cx="8" cy="8" r="7"/><path d="M1 8h14M8 1c-3 4-3 10 0 14M8 1c3 4 3 10 0 14" stroke="#fff" stroke-width="1" fill="none"/></svg>www.<span class="hl">PineHollow</span>.at</li>
    </ul>
    <svg class="stripe" viewBox="0 0 520 297" preserveAspectRatio="none" aria-hidden="true">
      <polygon points="0,288 380,250 520,210 520,297 0,297" fill="var(--accent-blue)"/>
      <polygon points="0,293 380,262 520,225 520,297 0,297" fill="var(--brand-blue)"/>
      <polygon points="390,250 520,196 520,297 470,297" fill="var(--ink)"/>
    </svg>
  </section>
</body>
</html>
```